Website Design Project For New Online Service
World Wide Online Obituary Notification Service Needing Professional Design
Website Design Project For New Online Service  - Internet Services
Creative Brief
Internet Services
http://www.MournBeacon.net
MournBeacon.net is an online obituary notification service.
Mournbeacon.net was created because there are far too many situations where someone says something like "why isn't your husband golfing with us today?" which is responded to by "he passed away 2 years ago."
This is awkward and hurtful for everyone involved. But it isn't the individuals fault! Society depends on newspapers for this information and nowadays it seems like another newspapers is declaring bankruptcy every month. They just don't work with todays fast paced lifestyle! So what does work with todays lifestyle? email, texting, tweeting and other electronic communication that delivers the information you want, when you want it!
MournBeacon allows individuals to sign up for an account and upload their email contact list from any major provider and receive a notification directly to their email if someone from this list passes away. Saving you the time of checking obituaries and keeping you informed!
MournBeacon.net "Stay close to those you love"
Modern
Blue (as seen in our symbol)
Grey (as seen in out symbol)
Looking forward to seeing the entries. Thanks to everyone who submits something!

```html
<!DOCTYPE html>
<html lang="en">
<head>
<meta charset="utf-8">
<title>MournBeacon.net</title>
<link rel="stylesheet" href="https://fonts.googleapis.com/css2?family=Open+Sans:wght@300;400;600;700&display=swap">
<style>
:root{
  --blue:#1c7fc4;
  --blue-dark:#0f5f99;
  --navy:#1e4f7d;
  --grey-text:#6d6d6d;
  --grey-light:#e9e9e9;
  --hero-grey:#e4e4e4;
  --nav-dark:#3a3a3a;
  --footer:#343434;
  --footer-text:#bdbdbd;
  --white:#ffffff;
}
*{box-sizing:border-box;margin:0;padding:0}
html,body{width:1200px;height:1107px;overflow:hidden}
body{font-family:"Open Sans",Arial,sans-serif;background:var(--white);color:var(--grey-text);position:relative}
.site-header{position:absolute;left:0;top:0;width:1200px;height:120px}
.brand{position:absolute;left:142px;top:18px;display:flex;align-items:center;gap:12px}
.brand-mark{width:58px;height:58px;background:var(--navy)}
.brand-name{font-size:30px;font-weight:700;color:var(--navy);letter-spacing:.5px}
.brand-tagline{position:absolute;left:212px;top:76px;font-size:13px;color:var(--grey-text);font-style:italic}
.login{position:absolute;left:604px;top:36px;display:flex;gap:12px;align-items:center}
.login-field{width:136px;height:28px;border:1px solid #cfcfcf;border-radius:4px;font-size:11px;color:#999;padding:6px 10px}
.login-button{width:64px;height:28px;border-radius:5px;background:var(--blue);color:var(--white);font-size:11px;font-weight:700;text-align:center;line-height:28px}
.login-links{position:absolute;left:604px;top:76px;font-size:11px;color:var(--grey-text)}
.login-links span{margin:0 4px}
.main-nav{position:absolute;left:140px;top:126px;width:908px;height:70px;background:linear-gradient(#4a4a4a,var(--nav-dark));border-radius:4px;display:flex;justify-content:flex-end;align-items:center}
.main-nav a{color:var(--white);text-decoration:none;font-size:18px;padding:0 30px;border-left:1px solid #555;line-height:70px}
.hero{position:absolute;left:0;top:208px;width:1200px;height:334px;background:linear-gradient(#f2f2f2,var(--hero-grey))}
.hero-title{position:absolute;left:140px;top:58px;font-size:30px;font-weight:300;color:#8a8a8a;line-height:1.45;white-space:nowrap;z-index:1}
.hero-title span{display:block;padding-left:146px}
.hero-photo{position:absolute;left:510px;top:16px;width:530px;height:290px;background:radial-gradient(ellipse at 50% 45%,#c9b7a6,#d9d3cd 55%,#e4e4e4 80%)}
.hero-arrow{position:absolute;top:110px;width:30px;height:64px;background:#d2d2d2}
.hero-arrow.prev{left:0}.hero-arrow.next{right:0}
.accounts{position:absolute;top:580px;width:438px}
.accounts.user{left:140px}.accounts.funeral{left:630px;width:418px}
.accounts h2{font-size:19px;font-weight:400;color:var(--blue);text-transform:uppercase;border-bottom:1px solid #ddd;padding-bottom:10px}
.accounts p{font-size:12px;line-height:1.6;margin-top:16px}
.cta{margin-top:22px;display:flex;align-items:center;justify-content:space-between;width:310px;height:40px;background:var(--blue);border-radius:20px;color:var(--white);font-size:14px;font-weight:600;padding:0 8px 0 30px}
.cta-arrow{width:26px;height:26px;border-radius:50%;background:var(--white)}
.site-footer{position:absolute;left:0;top:888px;width:1200px;height:219px;background:var(--footer);color:var(--footer-text)}
.badges{position:absolute;left:140px;top:22px;display:flex;gap:22px;align-items:flex-end}
.badge-seal{width:120px;height:66px;background:#e8d24a;border-radius:6px}
.badge-shield{width:78px;height:150px;background:#1a4f86}
.badge-round{width:140px;height:140px;border-radius:50%;background:#dfe9f3}
.footer-links{position:absolute;left:590px;top:38px;list-style:none;border-left:1px solid #555;padding-left:12px;font-size:12px;line-height:22px}
.connect{position:absolute;left:850px;top:36px;font-size:12px}
.social{display:flex;gap:8px;margin-top:8px}
.social span{width:22px;height:22px;border-radius:50%;background:var(--blue)}
.page-count{position:absolute;left:1020px;top:118px;font-size:11px}
.copyright{position:absolute;left:0;bottom:10px;width:1200px;text-align:center;font-size:10px}
</style>
</head>
<body>
<header class="site-header">
  <div class="brand"><div class="brand-mark"></div><div class="brand-name">MournBeacon.net</div></div>
  <div class="brand-tagline">Stay close to those you love</div>
  <div class="login">
    <div class="login-field">E-mail</div>
    <div class="login-field">Password</div>
    <div class="login-button">SIGN IN</div>
  </div>
  <div class="login-links">Create User Account<span>|</span>Funeral Home Registration<span>|</span>Forgot Password?</div>
</header>

<nav class="main-nav">
  <a href="#">Home</a>
  <a href="#">How it works / FAQ</a>
  <a href="#">Contact us / Help</a>
</nav>

<section class="hero">
  <div class="hero-arrow prev"></div>
  <div class="hero-photo" role="img" aria-label="Photo of a smiling family of four lying together on the floor"></div>
  <h1 class="hero-title">Everyone has had<span>a time when...</span></h1>
  <div class="hero-arrow next"></div>
</section>

<section class="accounts user">
  <h2>User Accounts</h2>
  <p>Checking the obituaries too often? Worrying that you'll miss an obituary? Here is your peace of mind! MournBeacon.net eliminates these concerns by notifying you in the unfortunate event that a friend, colleague or loved one passes away.</p>
  <div class="cta">Sign up for an MournBeacon.net<span class="cta-arrow"></span></div>
</section>

<section class="accounts funeral">
  <h2>Funeral Home Accounts</h2>
  <p>Traditional methods of obituaries are no longer keeping up with our society. We don't have time to be checking all the newspapers of where our friends, family or even clients are located. But we still need to be informed when someone passes away.</p>
  <p>Join the Next Generation Obituary Notification Service. Send an obituary notification directly to the people who need this information, and allow your clients to focus on the important situation at hand.</p>
  <div class="cta">Register a Funeral Home Accounts<span class="cta-arrow"></span></div>
</section>

<footer class="site-footer">
  <div class="badges">
    <div class="badge-seal"></div>
    <div class="badge-shield"></div>
    <div class="badge-round"></div>
  </div>
  <ul class="footer-links">
    <li>Our Services</li><li>Return Policy</li><li>Delivery Policy</li><li>Privacy Policy</li><li>Contact Us</li>
  </ul>
  <div class="connect">Connect with us<div class="social"><span></span><span></span></div></div>
  <div class="page-count">421</div>
  <div class="copyright">Copyright © 2012 MournBeacon.net. All rights reserved. | ®™ Trademarks of SkyPoints Trading Co. Used under license by Rewardline, Inc. and MournBeacon.net</div>
</footer>
</body>
</html>
```